Realty Group Needs Classy, Contemporary Letterhead Design

We need a letterhead design for a new realty company located in NY, USA. We buy investment properties to rehabilitate and or keep in our rental portfolio.

```html
<!DOCTYPE html>
<html lang="en">
<head>
<meta charset="utf-8">
<title>Meridian Realty Group — Letterhead</title>
<link rel="stylesheet" href="https://fonts.googleapis.com/css2?family=Open+Sans:wght@400&family=Poppins:wght@400;500;700&display=swap">
<style>
  :root {
    --backdrop: #dcdcdc;
    --paper: #f8f8f8;
    --brand-purple: #4a2a86;
    --body-text: #555555;
    --footer-text: #4d4d4d;
    --signature-tone: #e6e6e6;
  }
  * { margin: 0; padding: 0; box-sizing: border-box; }
  html, body {
    width: 1153px;
    height: 1200px;
    overflow: hidden;
    background: var(--backdrop);
  }
  .letterhead {
    position: absolute;
    left: 160px;
    top: 20px;
    width: 832px;
    height: 1160px;
    background: var(--paper);
  }
  .brand-name {
    position: absolute;
    right: 76px;
    top: 86px;
    font-family: "Poppins", sans-serif;
    font-weight: 700;
    font-size: 27px;
    letter-spacing: 0.3px;
    color: var(--brand-purple);
    white-space: nowrap;
  }
  .letter-body {
    position: absolute;
    left: 74px;
    top: 272px;
    width: 682px;
    font-family: "Open Sans", sans-serif;
    font-size: 15.2px;
    line-height: 22.4px;
    color: var(--body-text);
  }
  .letter-body p {
    text-align: justify;
    margin-bottom: 22.4px;
  }
  .letter-body .salutation,
  .letter-body .closing { text-align: left; }
  .signature-area {
    position: absolute;
    left: 76px;
    top: 866px;
    width: 98px;
    height: 92px;
    background: var(--signature-tone);
    border-radius: 4px;
  }
  .footer {
    position: absolute;
    left: 0;
    right: 0;
    top: 1047px;
    text-align: center;
    font-family: "Poppins", sans-serif;
    font-size: 15px;
    line-height: 19.5px;
    color: var(--footer-text);
  }
  .footer .company { color: var(--brand-purple); font-weight: 500; }
  .contact-line { display: flex; justify-content: center; align-items: center; gap: 10px; }
  .contact-item { display: inline-flex; align-items: center; gap: 5px; }
  .contact-item svg { width: 13px; height: 13px; fill: var(--brand-purple); }
</style>
</head>
<body>
  <main class="letterhead">
    <div class="brand-name">Meridian Realty Group</div>

    <section class="letter-body">
      <p class="salutation">Dear customer,</p>
      <p>Lorem ipsum dolor sit amet, consectetur adipisicing elit, sed do eiusmod tempor incididunt ut labore et dolore magna aliqua. Ut enim ad minim veniam, quis nostrud exercitation ullamco laboris nisi ut aliquip ex ea commodo consequat. Duis aute irure dolor in reprehenderit in voluptate velit esse cillum dolore eu fugiat nulla pariatur. Excepteur sint occaecat cupidatat non proident, sunt in culpa qui officia deserunt mollit anim id est laborum.</p>
      <p>Lorem ipsum dolor sit amet, consectetur adipisicing elit, sed do eiusmod tempor incididunt ut labore et dolore magna aliqua. Ut enim ad minim veniam, quis nostrud exercitation ullamco laboris nisi ut aliquip ex ea commodo consequat. Duis aute irure dolor in reprehenderit in voluptate velit esse cillum dolore eu fugiat nulla pariatur. Excepteur sint occaecat cupidatat non proident, sunt in culpa qui officia deserunt mollit anim id est laborum.</p>
      <p>Lorem ipsum dolor sit amet, consectetur adipisicing elit, sed do eiusmod tempor incididunt ut labore et dolore magna aliqua. Ut enim ad minim veniam, quis nostrud exercitation ullamco laboris nisi ut aliquip ex ea commodo consequat. Duis aute irure dolor in reprehenderit in voluptate velit esse cillum dolore eu fugiat nulla pariatur. Excepteur sint occaecat cupidatat non proident, sunt in culpa qui officia deserunt mollit anim id est laborum.</p>
      <p>Lorem ipsum dolor sit amet, consectetur adipisicing elit, sed do eiusmod tempor incididunt ut labore et dolore magna aliqua. Ut enim ad minim veniam, quis nostrud exercitation ullamco laboris nisi ut aliquip ex ea commodo consequat. Duis aute irure dolor in reprehenderit.</p>
      <p class="closing">Yours Sincerely,</p>
    </section>

    <div class="signature-area" role="img" aria-label="Handwritten signature"></div>

    <footer class="footer">
      <div class="company">Meridian Realty Group, LLC</div>
      <div class="address">48 Harbor View Lane, Eastbrook, NY 11790</div>
      <div class="contact-line">
        <span class="contact-item">
          <svg viewBox="0 0 16 16" aria-hidden="true"><path d="M2 5c0-2 2-3 6-3s6 1 6 3v1.5h-3V5H5v1.5H2z"/><path d="M4 8l1.5-2h5L12 8v5H4z"/></svg>
          555.214.0187
        </span>
        <span class="contact-item">
          <svg viewBox="0 0 16 16" aria-hidden="true"><path d="M1 3h14v10H1z M2 4.2v.6l6 4 6-4v-.6z" fill-rule="evenodd"/></svg>
          hello@meridianrealty.com
        </span>
        <span class="contact-item">
          <svg viewBox="0 0 16 16" aria-hidden="true"><circle cx="8" cy="8" r="7"/><path d="M5 4c2 0 2 2 4 2s1 3-1 3-1 3-3 2z M10 10c1 0 2 1 2 2-1 1-2 0-2-2z" fill="#f8f8f8"/></svg>
          www.meridianrealty.com
        </span>
      </div>
    </footer>
  </main>
</body>
</html>
```